A4 Single Sided Brochure Folder Design Technical Company

We are a technical company based in the UK, working worldwide for Power Distribution companies.

We have technical literature and need a folder to present these in. The design should be very simple and clean using our logo and "Innovative Utility Solutions"

Our website kormesa.com gives and idea of the business but don't follow the look of the website as we will be redoing shortly.

Requirements
Must have
• Logo and Strap Line
Nice to have
• Clean, easy to print and timeless
Should not have
• Shouldn't be fashionable, we certainly aren't

```html
<!DOCTYPE html>
<html lang="en">
<head>
<meta charset="utf-8">
<title>Kormesa Presentation Folder</title>
<link rel="stylesheet" href="https://fonts.googleapis.com/css2?family=Lato:wght@300;400&display=swap">
<style>
  :root {
    --backdrop: #e8e5e1;
    --paper: #ffffff;
    --crease: #c9b8b0;
    --brand-magenta: #b82e88;
    --tagline-plum: #4e1d44;
    --url-plum: #5a2a50;
    --logo-white: #ffffff;
  }
  html, body {
    margin: 0;
    padding: 0;
    width: 1200px;
    height: 1200px;
    overflow: hidden;
    background: var(--backdrop);
  }
  .folder-dieline {
    display: block;
    width: 1200px;
    height: 1200px;
  }
  .panel, .pocket, .glue-flap { fill: var(--paper); }
  .crease-line { stroke: var(--crease); stroke-width: 0.8; fill: none; }
  .brand-band { fill: var(--brand-magenta); }
  .brand-name {
    font-family: "Lato", sans-serif;
    font-weight: 300;
    font-size: 80px;
    fill: var(--logo-white);
  }
  .strapline {
    font-family: "Lato", sans-serif;
    font-weight: 300;
    font-size: 24px;
    fill: var(--tagline-plum);
  }
  .web-address {
    font-family: "Lato", sans-serif;
    font-weight: 400;
    font-size: 11.5px;
    fill: var(--url-plum);
  }
</style>
</head>
<body>
<svg class="folder-dieline" viewBox="0 0 1200 1200" xmlns="http://www.w3.org/2000/svg" role="img" aria-label="Kormesa A4 presentation folder, flat dieline">
  <g class="cover">
    <rect class="panel" x="106" y="138" width="1020" height="712"/>
    <rect class="brand-band" x="106" y="487" width="1020" height="192"/>
    <text class="web-address" x="315" y="598">www.kormesa.com</text>
    <text class="brand-name" x="870" y="602" text-anchor="middle">Kormesa</text>
    <text class="strapline" x="871" y="654" text-anchor="middle">Innovative Utility Solutions</text>
  </g>
  <g class="inside-pocket">
    <polygon class="glue-flap" points="70,860 106,850 106,1061 70,1055"/>
    <polygon class="pocket" points="106,850 616,850 546,1061 106,1061"/>
    <line class="crease-line" x1="106" y1="850" x2="616" y2="850"/>
    <line class="crease-line" x1="106" y1="850" x2="106" y2="1061"/>
  </g>
</svg>
</body>
</html>
```